Need a Basketball Court Design

We are replacing our current basketball court (gym floor) and we are looking for a new design. Our team is the “Harrowgate Falcons”. Our mascot is a “Knight” (in shining armor). Our colors are royal blue/grey/black. We are looking for a design that is contemporary and energetic.
The background of the court should display a “castle”. In the center of the court should be a team logo. You can use one of our existing logos or create your own. Along the baseline of the court should read the word “Harrowgate”.
I’ve attached ...
1) a picture of the current court
2) a mock-up design of what we are thinking
3) some of the different team logos we use.
Look and feel
Each slider illustrates characteristics of the customer's brand and the style your logo design should communicate.

```html
<!DOCTYPE html>
<html lang="en">
<head>
<meta charset="utf-8">
<title>Harrowgate Falcons – Court Design</title>
<link href="https://fonts.googleapis.com/css2?family=Roboto+Slab:wght@800&family=Oswald:wght@700&display=swap" rel="stylesheet">
<style>
  :root {
    --royal: #2f4d96;
    --royal-deep: #1f3c8a;
    --wood: #f1c47f;
    --wood-light: #f6d196;
    --line: #ffffff;
    --castle: #f8e6c6;
    --rim: #e8641e;
    --steel: #a9a9a9;
    --pad: #1c1c1c;
  }
  html, body {
    margin: 0;
    padding: 0;
    width: 1200px;
    height: 762px;
    overflow: hidden;
    background: var(--royal);
  }
  .court {
    display: block;
    width: 1200px;
    height: 762px;
  }
  .surround { fill: var(--royal); }
  .floor { fill: url(#floor-grain); }
  .court-line { fill: none; stroke: var(--line); stroke-width: 3; }
  .court-line--dashed { stroke-dasharray: 9 7; }
  .key { fill: var(--royal); stroke: var(--line); stroke-width: 3; }
  .castle-art { fill: var(--castle); opacity: 0.85; }
  .baseline-name {
    font-family: "Roboto Slab", serif;
    font-weight: 800;
    font-size: 30px;
    letter-spacing: 2px;
    fill: var(--line);
  }
  .team-name {
    font-family: "Oswald", sans-serif;
    font-weight: 700;
    fill: var(--royal-deep);
    text-anchor: middle;
  }
  .team-name--side { font-size: 26px; }
  .team-name--centre { font-size: 30px; }
  .backboard { fill: var(--pad); }
  .stanchion { fill: var(--steel); }
  .pad { fill: var(--pad); }
  .rim { fill: none; stroke: var(--rim); stroke-width: 4; }
  .net { fill: none; stroke: var(--line); stroke-width: 2; }
</style>
</head>
<body>
<svg class="court" viewBox="0 0 1166 740" preserveAspectRatio="none" xmlns="http://www.w3.org/2000/svg">
  <defs>
    <linearGradient id="floor-grain" x1="0" y1="0" x2="0" y2="1">
      <stop offset="0" stop-color="var(--wood-light)"/>
      <stop offset="0.5" stop-color="var(--wood)"/>
      <stop offset="1" stop-color="var(--wood-light)"/>
    </linearGradient>
  </defs>

  <!-- surround -->
  <rect class="surround" x="0" y="0" width="1166" height="740"/>

  <!-- playing surface -->
  <rect class="floor" x="75" y="60" width="1018" height="620"/>

  <!-- castle art areas -->
  <rect class="castle-art" x="192" y="478" width="252" height="196" role="img" aria-label="Castle illustration with towers and flags, faint on the floor"/>
  <rect class="castle-art" x="716" y="66" width="252" height="196" role="img" aria-label="Castle illustration with towers and flags, faint on the floor, upside down"/>

  <!-- keys -->
  <rect class="key" x="75" y="290" width="230" height="160"/>
  <rect class="key" x="863" y="290" width="230" height="160"/>

  <!-- boundary and midline -->
  <rect class="court-line" x="75" y="60" width="1018" height="620"/>
  <line class="court-line" x1="584" y1="60" x2="584" y2="680"/>
  <circle class="court-line" cx="584" cy="370" r="80"/>

  <!-- sideline ticks -->
  <g class="court-line">
    <line x1="415" y1="38" x2="415" y2="60"/>
    <line x1="748" y1="38" x2="748" y2="60"/>
    <line x1="415" y1="680" x2="415" y2="702"/>
    <line x1="748" y1="680" x2="748" y2="702"/>
  </g>

  <!-- left half -->
  <path class="court-line" d="M75,133 L130,133 A237.5,237.5 0 1 1 130,607 L75,607"/>
  <path class="court-line" d="M305,290 A80,80 0 0 1 305,450"/>
  <path class="court-line court-line--dashed" d="M305,290 A80,80 0 0 0 305,450"/>
  <g class="court-line">
    <line x1="170" y1="280" x2="170" y2="290"/>
    <line x1="215" y1="280" x2="215" y2="290"/>
    <line x1="250" y1="280" x2="250" y2="290"/>
    <line x1="288" y1="280" x2="288" y2="290"/>
    <line x1="170" y1="450" x2="170" y2="460"/>
    <line x1="215" y1="450" x2="215" y2="460"/>
    <line x1="250" y1="450" x2="250" y2="460"/>
    <line x1="288" y1="450" x2="288" y2="460"/>
  </g>

  <!-- right half -->
  <path class="court-line" d="M1093,133 L1038,133 A237.5,237.5 0 1 0 1038,607 L1093,607"/>
  <path class="court-line" d="M863,290 A80,80 0 0 0 863,450"/>
  <path class="court-line court-line--dashed" d="M863,290 A80,80 0 0 1 863,450"/>
  <g class="court-line">
    <line x1="998" y1="280" x2="998" y2="290"/>
    <line x1="953" y1="280" x2="953" y2="290"/>
    <line x1="918" y1="280" x2="918" y2="290"/>
    <line x1="880" y1="280" x2="880" y2="290"/>
    <line x1="998" y1="450" x2="998" y2="460"/>
    <line x1="953" y1="450" x2="953" y2="460"/>
    <line x1="918" y1="450" x2="918" y2="460"/>
    <line x1="880" y1="450" x2="880" y2="460"/>
  </g>

  <!-- left goal -->
  <g class="goal goal--left">
    <rect class="pad" x="12" y="323" width="40" height="94" rx="8"/>
    <polygon class="stanchion" points="50,360 70,360 95,335 95,345 78,365 95,390 95,400 70,375 50,375"/>
    <rect class="backboard" x="94" y="322" width="6" height="96"/>
    <circle class="rim" cx="125" cy="368" r="17"/>
    <circle class="net" cx="125" cy="368" r="11"/>
  </g>

  <!-- right goal -->
  <g class="goal goal--right">
    <rect class="pad" x="1114" y="323" width="40" height="94" rx="8"/>
    <polygon class="stanchion" points="1116,360 1096,360 1071,335 1071,345 1088,365 1071,390 1071,400 1096,375 1116,375"/>
    <rect class="backboard" x="1066" y="322" width="6" height="96"/>
    <circle class="rim" cx="1041" cy="368" r="17"/>
    <circle class="net" cx="1041" cy="368" r="11"/>
  </g>

  <!-- team names on the floor -->
  <text class="team-name team-name--side" x="415" y="150">HARROWGATE FALCONS</text>
  <text class="team-name team-name--side" x="750" y="602" transform="rotate(180 750 593)">HARROWGATE FALCONS</text>

  <!-- centre court name -->
  <text class="team-name team-name--centre" x="584" y="362">HARROWGATE</text>
  <text class="team-name team-name--centre" x="584" y="398">FALCONS</text>

  <!-- baseline names -->
  <text class="baseline-name" x="0" y="0" text-anchor="middle" transform="translate(48 550) rotate(-90)">HARROWGATE</text>
  <text class="baseline-name" x="0" y="0" text-anchor="middle" transform="translate(1120 190) rotate(90)">HARROWGATE</text>
</svg>
</body>
</html>
```